Promotional Flyer - Refer A friend for QPN (Rebranding)

We have an exsisting Promotion flyer that we would like upgraded to the standards of our other newly designed flyers - all attached for viewing.

The flyer is for a promotion we run called "Refer a Friend".

The flyer needs to be in line with our current branding scheme, simple, easy to read and consumer engageing and Must haves etc. are to be followed.

Information as follows:

Terms and Conditions - Eligible names are dran at random twice a year, January - June (Drawn in July) and July - December (drawn in January). Friend reffered must have place name of refferrer on enrolment application form and both student and reffered student must have completed their course to be eligible. (withdrawals are not eligble). Winning students must be available to pick up the Gift Card from our Kelderby head office and have their photo taken for advertising purposes.

Main Call to action - "Refer a friend for 2016 and you could win a $500 Gift Card."

Have one testomonial on flyer - "Deciding to take my course at Verdant Skills Academy was the best decision. I am now employed in a field that gives me personal satisfaction daily."- Ned, Aged Care/HACC & Health Services Student.

Target Market(s)

Current students both male & female between the ages of 30 - 45 years.

Industry/Entity Type

Education

Font styles to use
Serif
Sans Serif

Colors
f37122
f78f20
fece3e

Requirements
Must have
• Our flyer must have the following information:
• TOID. 47193
• Logo
• Scheme must be in line with our current branding - can view website and other flyers attached for reference
• Images relevant to brief - see dropbox link for image choice: https://www.filecrate-share.com/sh/k4tqw9m2zpx7rb/BBXyRpLk-omTgZnQ2wVsJeulc?dl=0
• Engaging look & Feel to the flyer
• Website - www.verdantskillsacademy.edu.au
• Social Media buttons - Facebook, Twitter, Instagram, Youtube & LinkedIn
• Phone number - 03 5127 6481
• Must include all details as indicated in project description and previous flyer used.
• Flyer must include a statement in small print at the bottom of the flyer on the right hand side saying "*Information stipulated in this brochure is current at time of printing. V2. 271015"
• Terms and conditions are essential to be added to this flyer.
• Have one testomonial on flyer - "Deciding to take my course at Verdant Skills Academy was the best decision. I am now employed in a field that gives me personal satisfaction daily."- Ned, Aged Care/HACC & Health Services Student.
Nice to have
• Fun, engageing additional imagery - happy smiling faces.
Should not have
• Fancy font
• Colours other than stipulated in colour scheme

```html
<!DOCTYPE html>
<html lang="en">
<head>
<meta charset="utf-8">
<title>Refer a Friend – Verdant Skills Academy</title>
<link rel="stylesheet" href="https://fonts.googleapis.com/css2?family=Arimo:ital,wght@0,400;0,700;1,400&display=swap">
<style>
  :root{
    --orange:#f37122;
    --amber:#f78f20;
    --yellow:#fece3e;
    --ink:#111111;
    --night:#1a1a1a;
    --paper:#ffffff;
  }
  *{box-sizing:border-box;margin:0;padding:0}
  html,body{width:847px;height:1200px;overflow:hidden;background:var(--paper)}
  body{font-family:"Arimo",Arial,sans-serif;color:var(--paper)}
  .flyer{position:relative;width:847px;height:1200px;background:var(--night);overflow:hidden}

  .hero-photo{position:absolute;left:0;top:0;width:847px;height:610px;
    background:linear-gradient(120deg,#f2f2f2 0%,#d9dcdf 22%,#6d737a 42%,#2c3036 62%,#3a4a6a 80%,#1b1e24 100%)}
  .hero-shade{position:absolute;left:0;top:180px;width:847px;height:430px;
    background:linear-gradient(180deg,rgba(0,0,0,0) 0%,rgba(0,0,0,.45) 35%,rgba(20,20,20,.9) 100%)}

  .brand{position:absolute;right:28px;top:40px;display:flex;align-items:center;gap:10px}
  .brand-dot{width:34px;height:34px;border-radius:50%;background:var(--orange)}
  .brand-name{font-weight:700;font-size:20px;color:var(--orange);width:130px;line-height:1.1}

  .headline{position:absolute;left:70px;top:215px;text-align:center;width:470px;font-size:inherit}
  .headline .lead{display:block;font-weight:700;font-size:44px;line-height:1.12;color:var(--paper)}
  .headline .amount{display:block;font-weight:700;font-size:150px;line-height:1;color:var(--amber);margin-top:2px}
  .headline .prize{display:block;font-weight:400;font-size:66px;line-height:1;color:var(--amber)}

  .ward-photo{position:absolute;left:30px;top:600px;width:345px;height:240px;
    background:linear-gradient(160deg,#cfd8dc 0%,#8fa3ad 45%,#4a5a63 100%)}

  .social{position:absolute;left:30px;top:855px;list-style:none}
  .social li{display:flex;align-items:center;gap:14px;height:38px;font-size:21px;color:var(--paper)}
  .social .icon{width:24px;height:24px;border-radius:50%;background:var(--paper);flex:none}
  .social .phone{width:24px;height:24px;flex:none}

  .terms{position:absolute;left:400px;top:612px;width:420px}
  .terms-title{height:54px;background:var(--orange);border-radius:6px 6px 0 0;
    font-weight:700;font-size:26px;line-height:54px;padding-left:30px;color:var(--paper);white-space:nowrap}
  .terms-body{background:linear-gradient(180deg,var(--yellow) 0%,var(--amber) 100%);
    padding:18px 18px 18px 22px;font-size:21px;line-height:1.25;color:var(--ink);height:428px}

  .testimonial{position:absolute;left:450px;top:1100px;width:370px;height:46px;background:var(--paper);
    color:var(--ink);font-style:italic;font-size:8.5px;line-height:1.25;padding:4px 8px;display:flex;gap:8px}
  .testimonial .quote{flex:1}
  .testimonial .author{width:96px;text-align:right;font-style:normal;font-weight:700;font-size:8px}

  .website{position:absolute;left:30px;top:1108px;font-size:22px;font-weight:700;color:var(--orange)}

  .footer{position:absolute;left:0;bottom:0;width:847px;height:50px;background:var(--paper);
    color:var(--ink);font-weight:700;font-size:19px;text-align:right;padding-right:22px;line-height:50px}
</style>
</head>
<body>
<main class="flyer">
  <div class="hero-photo" role="img" aria-label="Close-up of a gloved nurse placing a cannula in a patient's arm"></div>
  <div class="hero-shade"></div>

  <div class="brand">
    <span class="brand-dot"></span>
    <span class="brand-name">Verdant Skills Academy</span>
  </div>

  <h1 class="headline">
    <span class="lead">Refer a friend<br>and you could win a</span>
    <span class="amount">$500</span>
    <span class="prize">Gift card</span>
  </h1>

  <div class="ward-photo" role="img" aria-label="Hospital ward with an IV drip stand beside a bed"></div>

  <ul class="social">
    <li><span class="icon"></span>verdantskills</li>
    <li><span class="icon"></span>VSAMelbourne</li>
    <li><span class="icon"></span>verdant-skills-academy</li>
    <li><span class="icon"></span>vsakelderby</li>
    <li>
      <svg class="phone" viewBox="0 0 24 24" aria-hidden="true"><path fill="#fff" d="M6.6 10.8a15 15 0 0 0 6.6 6.6l2.2-2.2c.3-.3.7-.4 1-.2 1.1.4 2.3.6 3.6.6.6 0 1 .4 1 1V20c0 .6-.4 1-1 1A17 17 0 0 1 3 4c0-.6.4-1 1-1h3.5c.6 0 1 .4 1 1 0 1.3.2 2.5.6 3.6.1.3 0 .7-.2 1z"/></svg>
      03 5127 6481
    </li>
    <li><span class="icon"></span>Verdant Skills Academy</li>
  </ul>

  <section class="terms">
    <h2 class="terms-title">TERMS AND CONDITIONS</h2>
    <p class="terms-body">Game of chance, eligible names drawn at random twice a year - July- December (drawn in January) and January - June (drawn in July). Friend referred must have your name on enrolment form to be eligible. Both student and referred student must have completed the course (withdrawals are not eligible.) Winning students must be available to pick up Harbourline Gift Card and have photo taken for advertising purposes.</p>
  </section>

  <blockquote class="testimonial">
    <span class="quote">"Deciding to take my course at Verdant Skills Academy was the best decision. I am now employed in a field that gives me personal satisfaction daily."</span>
    <span class="author">Ned,<br>Aged Care/HACC &amp; Health Services Student.</span>
  </blockquote>

  <div class="website">www.verdantskillsacademy.edu.au</div>

  <footer class="footer">Information stipulated in this brochure is current at time of printing. V2. 271015</footer>
</main>
</body>
</html>
```